Kalm to Bloom: Prespective and Balence in People's Lives Needs a Buissness Card Design

Calm to Bloom Community Center is an organization that seeks to bring balance into people's lives. Main services include: guided meditation, group brainstorming, and guided counseling. Calm to Bloom combines Eastern practices, i.e. Buddhism, Hinduism, and Taoism, with Western practices: therapy, group brainstorming and healing. We would like a double sided card: 1) front vertical with image, 2) back horizontal with information. The main colors for the card are red, white, black. Different finishes would be nice--please no high gloss. Matte, pearlized, embossing--used tactfully and sparingly would be nice. The card should convey balance/harmony in a modern world.

```html
<!DOCTYPE html>
<html lang="en">
<head>
<meta charset="utf-8">
<title>Calm to Bloom – Business Card</title>
<link rel="stylesheet" href="https://fonts.googleapis.com/css2?family=Open+Sans:wght@400;600;700&display=swap">
<style>
  :root {
    --ink: #1b1716;
    --red: #d3261c;
    --paper: #ffffff;
    --paper-shade: #ececec;
    --stage: #3a3a3a;
    --muted: #222;
  }
  html, body {
    margin: 0;
    padding: 0;
    width: 1200px;
    height: 823px;
    overflow: hidden;
    background: var(--stage);
    font-family: "Open Sans", Arial, sans-serif;
  }
  .canvas {
    position: relative;
    width: 1200px;
    height: 823px;
  }
  .card {
    position: absolute;
    left: 280px;
    width: 640px;
    height: 366px;
    overflow: hidden;
    background: radial-gradient(ellipse at 55% 50%, var(--paper) 40%, var(--paper-shade) 100%);
    box-shadow: 0 6px 18px rgba(0,0,0,.45);
  }
  .card--front { top: 34px; }
  .card--back { top: 424px; }

  /* front */
  .front__band {
    position: absolute;
    left: 0; right: 0;
    top: 45%;
    height: 42%;
    background: var(--ink);
  }
  .front__mark {
    position: absolute;
    left: 50%;
    top: 62px;
    transform: translateX(-50%);
    display: flex;
    flex-direction: column;
    align-items: center;
    gap: 24px;
  }
  .front__dot {
    width: 120px;
    height: 120px;
    border-radius: 50%;
    background: var(--red);
  }
  .front__name {
    color: var(--paper);
    font-weight: 700;
    font-size: 26px;
    letter-spacing: 1px;
  }

  /* back */
  .back__strip {
    position: absolute;
    top: 0; bottom: 0;
    right: 0;
    width: 40px;
    background: var(--ink);
  }
  .back__rule {
    position: absolute;
    top: 0; bottom: 0;
    right: 48px;
    width: 5px;
    background: var(--red);
  }
  .back__mark {
    position: absolute;
    left: 40px;
    top: 190px;
    display: flex;
    align-items: center;
    gap: 12px;
  }
  .back__dot {
    width: 26px;
    height: 26px;
    border-radius: 50%;
    background: var(--red);
  }
  .back__name {
    color: var(--ink);
    font-weight: 700;
    font-size: 22px;
  }
  .info {
    position: absolute;
    left: 340px;
    top: 60px;
    color: var(--muted);
  }
  .info__company {
    font-weight: 700;
    font-size: 22px;
    letter-spacing: .5px;
    color: var(--ink);
    margin: 0 0 26px;
  }
  .info__person {
    font-size: 22px;
    margin: 0;
    color: var(--ink);
  }
  .info__person span { color: var(--red); }
  .info__role {
    font-size: 14px;
    margin: 0 0 22px;
  }
  .contact {
    list-style: none;
    margin: 0;
    padding: 0;
    font-size: 15px;
  }
  .contact li {
    display: flex;
    align-items: center;
    gap: 10px;
    height: 24px;
  }
  .contact svg {
    width: 14px;
    height: 14px;
    fill: var(--red);
    flex: none;
  }
</style>
</head>
<body>
<div class="canvas">

  <section class="card card--front" aria-label="Card front">
    <div class="front__band"></div>
    <div class="front__mark">
      <div class="front__dot"></div>
      <div class="front__name">Calm to Bloom</div>
    </div>
  </section>

  <section class="card card--back" aria-label="Card back">
    <div class="back__mark">
      <div class="back__dot"></div>
      <div class="back__name">Calm to Bloom</div>
    </div>

    <div class="info">
      <p class="info__company">CALM TO BLOOM</p>
      <p class="info__person"><span>Employee</span> Name</p>
      <p class="info__role">Designation</p>
      <ul class="contact">
        <li>
          <svg viewBox="0 0 14 14"><path d="M7 0a5 5 0 0 0-5 5c0 4 5 9 5 9s5-5 5-9a5 5 0 0 0-5-5zm0 7a2 2 0 1 1 0-4 2 2 0 0 1 0 4z"/></svg>
          123 Street, City, Country.
        </li>
        <li>
          <svg viewBox="0 0 14 14"><path d="M3 1l2.5 3-1.5 1.5a8 8 0 0 0 4.5 4.5L10 8.5l3 2.5-1.5 2C6 13 1 8 1 2.5z"/></svg>
          000-123-123
        </li>
        <li>
          <svg viewBox="0 0 14 14"><path d="M7 0a7 7 0 1 0 0 14A7 7 0 0 0 7 0zm0 1.3c.8.8 1.4 2.1 1.6 3.4H5.4C5.6 3.4 6.2 2.1 7 1.3zM1.4 6h2.8a11 11 0 0 0 0 2H1.4a5.7 5.7 0 0 1 0-2zm4 0h3.2a10 10 0 0 1 0 2H5.4a10 10 0 0 1 0-2zm4.4 0h2.8a5.7 5.7 0 0 1 0 2H9.8a11 11 0 0 0 0-2zM5.4 9.3h3.2c-.2 1.3-.8 2.6-1.6 3.4-.8-.8-1.4-2.1-1.6-3.4z"/></svg>
          hello@calmtobloom.org
        </li>
        <li>
          <svg viewBox="0 0 14 14"><path d="M0 3h14v1L7 8 0 4zm0 2.5L7 9.5l7-4V11H0z"/></svg>
          www.calmtobloom.org
        </li>
      </ul>
    </div>

    <div class="back__rule"></div>
    <div class="back__strip"></div>
  </section>

</div>
</body>
</html>
```